CBD Product Label Supplement Company

We need a label design for our CBD Immunity Gummies product. The CBD immunity gummies are strawberry flavored. Here's an example of one the top brands currently. https://www.brindlecove.com/cbd-dusk-rest-chew. Please don't make it look similar to that brand. That is just an example of a top brand currently. Our brand colors is simply green and white, logo included in files. We don't want a lot of colors in the design and don't want the design to be all over the place. we want multi colors 4 maybe 5 used. target audience is 30 years and older. Want to give it a nature feel while also conveying immunity. Attached screenshot will show standard label with ingredients and designations. We'd like all of those included on the label if possible. Vegetarian, Vegan, Non-Dairy, Gluten free, Non-Gmo. Ad " Vitamin C + Elderberry" to front of label as well.

Target Market(s)

30 to 65+ men and women. Pain Relief and Immunity Support Focused.

Industry/Entity Type

Supplement

Font styles to use
Serif
Sans Serif

Colors
9bcb3c
add136
00a990
33b8a4
ec1f27
f04a50
ffffff
6b449b

Requirements
Must have
• Informative label. Because we've combined CBD with Elderberry, Vitamin C, Vitamin A, Vitamin E to help with Immunity we want that to be known. Elderberry, Vitamin C are the two most important vitamins of that mix. Product designation labels, Vegetarian, Vegan, Non-Dairy, Gluten free, Non-Gmo. Gummies are strawberry flavored so would like some redish, pink somewhere in label.
Should not have
• no browns, grays, oranges, yellow,

```html
<!DOCTYPE html>
<html lang="en">
<head>
<meta charset="utf-8">
<title>Solvina Nutrition – CBD Immunity Gummies Labels</title>
<link href="https://fonts.googleapis.com/css2?family=Arimo:wght@400;700&family=Oswald:wght@400;500;600&family=Nunito+Sans:wght@300;800&family=Kaushan+Script&family=Libre+Baskerville:wght@700&display=swap" rel="stylesheet">
<style>
  :root{
    --stage:#f3ebf6;
    --teal:#1fa597;
    --mint:#c8ebe4;
    --mint-deep:#9fd8cd;
    --berry:#e3365a;
    --berry-dark:#c92a4b;
    --ink:#1b1b1b;
    --white:#ffffff;
  }
  *{box-sizing:border-box;margin:0;padding:0}
  html,body{width:1200px;height:403px;overflow:hidden}
  body{background:var(--stage);position:relative;font-family:"Arimo",sans-serif;color:var(--ink)}

  .label{position:absolute;top:88px;width:560px;height:210px;background:var(--teal);overflow:hidden}
  .label--a{left:20px}
  .label--b{left:620px;background:var(--mint)}
  .variant-mark{position:absolute;top:330px;width:560px;text-align:center;font:700 11px "Libre Baskerville",serif}
  .variant-mark--a{left:20px}
  .variant-mark--b{left:620px}

  /* barcode zone */
  .barcode-zone{position:absolute;left:0;top:0;width:36px;height:210px;background:var(--white);border-right:1px solid #ddd}
  .barcode-zone span{position:absolute;left:50%;top:50%;transform:translate(-50%,-50%) rotate(90deg);white-space:nowrap;font-size:7px}

  /* info panel */
  .info-panel{position:absolute;left:36px;top:0;width:156px;height:210px;color:var(--white);font-size:5.2px;line-height:1.25}
  .label--b .info-panel{color:var(--ink)}
  .info-panel p{position:absolute;left:6px;right:6px}
  .info-panel b{font-weight:700}
  .info-use{top:8px}
  .info-allergen{top:28px}
  .info-warning{top:64px}
  .info-keep{top:120px;font-weight:700;text-transform:uppercase}
  .info-hemp{top:150px}
  .label--b .info-warning{color:var(--white)}
  .disclaimer{position:absolute;left:8px;right:8px;top:176px;padding:3px 4px;background:var(--white);color:var(--ink);font-size:5px;line-height:1.2;text-align:center;border:1px solid #999}

  /* front panel */
  .front{position:absolute;left:192px;top:0;width:221px;height:210px;text-align:center}
  .front__top{position:absolute;left:0;top:0;width:221px;height:116px;background:#bfe6df}
  .front__bottom{position:absolute;left:0;top:116px;width:221px;height:94px;background:var(--berry)}

  .brand{position:absolute;left:0;right:0;top:16px;font:400 12px "Arimo",sans-serif;letter-spacing:2px;color:var(--ink);line-height:1}

  .title{position:absolute;left:0;right:0;top:40px;line-height:1}
  .label--a .title__main{font:600 31px "Oswald",sans-serif;color:var(--teal);letter-spacing:-.5px}
  .label--a .title__sub{font:800 16px "Nunito Sans",sans-serif;color:var(--teal);letter-spacing:1px;margin-top:2px}

  .band{position:absolute;left:36px;top:60px;width:524px;height:58px;background:var(--berry)}
  .label--b .title{top:68px}
  .label--b .title__main{font:800 22px "Nunito Sans",sans-serif;color:var(--white)}
  .label--b .title__sub{font:300 15px "Nunito Sans",sans-serif;color:var(--white);letter-spacing:4px;margin-top:3px}

  .flavor{position:absolute;left:0;right:0;top:121px;font:400 25px "Kaushan Script",cursive;color:var(--white);line-height:1.1}
  .dose{position:absolute;left:0;right:0;top:155px;font:700 7px "Arimo",sans-serif;color:var(--white)}
  .actives{position:absolute;left:0;right:0;top:166px;font:700 7.5px "Arimo",sans-serif;color:var(--white);letter-spacing:.4px}
  .label--b .flavor{color:var(--berry)}
  .label--b .dose{color:var(--ink)}
  .label--b .actives{color:var(--teal)}

  .claims{position:absolute;left:0;top:179px;width:221px;height:12px;display:flex;list-style:none}
  .claims li{flex:1 1 auto;font:500 5.4px "Oswald",sans-serif;color:var(--white);background:var(--berry-dark);display:flex;align-items:center;justify-content:center;border-right:1px solid var(--berry)}
  .label--b .claims li{background:var(--mint-deep);color:var(--ink);border-right-color:var(--mint)}
  .footer-line{position:absolute;left:0;right:0;top:195px;font:400 6px "Oswald",sans-serif;color:var(--white)}
  .footer-line span{margin:0 5px}
  .label--b .footer-line{color:var(--ink)}

  /* facts panel */
  .facts-panel{position:absolute;left:413px;top:0;width:147px;height:210px}
  .facts{position:absolute;left:6px;top:10px;width:135px;background:var(--white);border:1px solid var(--ink);padding:3px 4px;font-size:4.8px;line-height:1.25;color:var(--ink)}
  .facts h2{font:700 9px "Arimo",sans-serif;border-bottom:1px solid var(--ink);padding-bottom:1px}
  .facts__serving{font-weight:700;padding:2px 0;border-bottom:3px solid var(--ink)}
  .facts table{width:100%;border-collapse:collapse;table-layout:fixed}
  .facts col.c-name{width:66%}
  .facts col.c-amt{width:18%}
  .facts col.c-dv{width:16%}
  .facts td{padding:.5px 0;border-bottom:.5px solid var(--ink);vertical-align:top}
  .facts td:nth-child(2),.facts td:nth-child(3){text-align:right}
  .facts .dv-head td{font-weight:700;text-align:right}
  .facts__notes{border-top:2px solid var(--ink);padding-top:1px}
  .facts__other{border-top:2px solid var(--ink);margin-top:2px;padding-top:2px}
  .manufactured{position:absolute;left:6px;top:176px;font:700 5px "Arimo",sans-serif;color:var(--white)}
  .label--b .manufactured{color:var(--ink)}
</style>
</head>
<body>

<!-- Label A -->
<section class="label label--a" aria-label="Label version A">
  <div class="barcode-zone"><span>Bar-Code Zone</span></div>

  <div class="info-panel">
    <p class="info-use"><b>Suggested Use:</b> Adults, take one (1) gummy daily as a dietary supplement.</p>
    <p class="info-allergen"><b>ALLERGEN WARNING:</b> Packaged in the same facility as peanuts, tree nuts, wheat, soy and milk products.</p>
    <p class="info-warning"><b>WARNING:</b> Do not exceed recommended dose. Pregnant or nursing mothers, children under 18, and individuals with a known medical condition should consult a physician before using this or any dietary supplement.</p>
    <p class="info-keep">Keep out of reach of children. Store at room temperature. Do not use if safety seal is damaged or missing.</p>
    <p class="info-hemp">Natural Cannabidiol Derived from<br>US Grown Hemp.</p>
    <div class="disclaimer">†These statements have not been evaluated by the FDA. This product is not intended to diagnose, cure, treat or prevent any disease.</div>
  </div>

  <div class="front">
    <div class="front__top" role="img" aria-label="Soft teal chevron texture"></div>
    <div class="front__bottom" role="img" aria-label="Strawberry red chevron texture"></div>
    <div class="brand">SOLVINA NUTRITION</div>
    <div class="title">
      <div class="title__main">CBD Immunity</div>
      <div class="title__sub">GUMMIES</div>
    </div>
    <div class="flavor">Strawberry</div>
    <div class="dose">10 mg</div>
    <div class="actives">VITAMIN C + ELDERBERRY</div>
    <ul class="claims">
      <li>VEGETARIAN</li><li>VEGAN</li><li>NON-DAIRY</li><li>GLUTEN FREE</li><li>NON-GMO</li>
    </ul>
    <div class="footer-line"><span>30 GUMMIES</span><span>DIETARY SUPPLEMENT</span></div>
  </div>

  <div class="facts-panel">
    <div class="facts">
      <h2>Supplement Facts</h2>
      <div class="facts__serving">Serving Size: 1 Gummy<br>Servings Per Container: 30</div>
      <table>
        <colgroup><col class="c-name"><col class="c-amt"><col class="c-dv"></colgroup>
        <tr class="dv-head"><td colspan="3">% DV</td></tr>
        <tr><td>Vitamin C</td><td>50mg</td><td>56%</td></tr>
        <tr><td>Vitamin E</td><td>5mg</td><td>33%</td></tr>
        <tr><td>Vitamin B6</td><td>0.5mg</td><td>29%</td></tr>
        <tr><td>Elderberry</td><td>50mg</td><td>**</td></tr>
        <tr><td>Water Soluble CBD Powder (Maltodextrin, MCT, Naturally Occurring Cannabinoids)</td><td>10mg</td><td>**</td></tr>
      </table>
      <div class="facts__notes">* % Daily Value Based on 2,000 Calorie Diet<br>** Daily Value Not Established</div>
      <div class="facts__other"><b>Other Ingredients:</b> Tapioca Syrup, Organic Cane Sugar, Pear Juice, Pectin, Citric Acid, Sodium Citrate, Malic Acid, Natural Flavors, Natural Colors (Black Carrot).</div>
    </div>
    <div class="manufactured">Manufactured for:</div>
  </div>
</section>
<div class="variant-mark variant-mark--a">A</div>

<!-- Label B -->
<section class="label label--b" aria-label="Label version B">
  <div class="band"></div>
  <div class="barcode-zone"><span>Bar-Code Zone</span></div>

  <div class="info-panel">
    <p class="info-use"><b>Suggested Use:</b> Adults, take one (1) gummy daily as a dietary supplement.</p>
    <p class="info-allergen"><b>ALLERGEN WARNING:</b> Packaged in the same facility as peanuts, tree nuts, wheat, soy and milk products.</p>
    <p class="info-warning"><b>WARNING:</b> Do not exceed recommended dose. Pregnant or nursing mothers, children under 18, and individuals with a known medical condition should consult a physician before using this or any dietary supplement.</p>
    <p class="info-keep">Keep out of reach of children. Store at room temperature. Do not use if safety seal is damaged or missing.</p>
    <p class="info-hemp">Natural Cannabidiol Derived from<br>US Grown Hemp.</p>
    <div class="disclaimer">†These statements have not been evaluated by the FDA. This product is not intended to diagnose, cure, treat or prevent any disease.</div>
  </div>

  <div class="front">
    <div class="brand">SOLVINA NUTRITION</div>
    <div class="title">
      <div class="title__main">CBD Immunity</div>
      <div class="title__sub">GUMMIES</div>
    </div>
    <div class="flavor">Strawberry</div>
    <div class="dose">10 mg</div>
    <div class="actives">VITAMIN C + ELDERBERRY</div>
    <ul class="claims">
      <li>VEGETARIAN</li><li>VEGAN</li><li>NON-DAIRY</li><li>GLUTEN FREE</li><li>NON-GMO</li>
    </ul>
    <div class="footer-line"><span>30 GUMMIES</span><span>DIETARY SUPPLEMENT</span></div>
  </div>

  <div class="facts-panel">
    <div class="facts">
      <h2>Supplement Facts</h2>
      <div class="facts__serving">Serving Size: 1 Gummy<br>Servings Per Container: 30</div>
      <table>
        <colgroup><col class="c-name"><col class="c-amt"><col class="c-dv"></colgroup>
        <tr class="dv-head"><td colspan="3">% DV</td></tr>
        <tr><td>Vitamin C</td><td>50mg</td><td>56%</td></tr>
        <tr><td>Vitamin E</td><td>5mg</td><td>33%</td></tr>
        <tr><td>Vitamin B6</td><td>0.5mg</td><td>29%</td></tr>
        <tr><td>Elderberry</td><td>50mg</td><td>**</td></tr>
        <tr><td>Water Soluble CBD Powder (Maltodextrin, MCT, Naturally Occurring Cannabinoids)</td><td>10mg</td><td>**</td></tr>
      </table>
      <div class="facts__notes">* % Daily Value Based on 2,000 Calorie Diet<br>** Daily Value Not Established</div>
      <div class="facts__other"><b>Other Ingredients:</b> Tapioca Syrup, Organic Cane Sugar, Pear Juice, Pectin, Citric Acid, Sodium Citrate, Malic Acid, Natural Flavors, Natural Colors (Black Carrot).</div>
    </div>
    <div class="manufactured">Manufactured for:</div>
  </div>
</section>
<div class="variant-mark variant-mark--b">B</div>

</body>
</html>
```